contemporary upscale hair salon

we need a business card design for a modern upscale salon. I would like the card to be vertical, simple, and easy to read. I would like a black matte finish on the info side with white on the back of the card, white lettering with a splash of red incorporated somewhere in there. I also want to incorporate embossing and/or cut out in the letters. The info I would like; Name of the business (Velora Salon) stylist name (Janet) phone number(4075319264) and web address (www.veloraexample.com) I am open to putting shears on the card but without it looking too cheap. Looking for something really modern and edgy. these are just ideas I have, but feel free to show me your creative ideas.
please note: the website is still under construction please do not use any images or colors off the web page. Also i currently do not have a logo, that will be a future project.

```html
<!DOCTYPE html>
<html lang="en">
<head>
<meta charset="utf-8">
<title>Velora Salon – Business Card</title>
<link href="https://fonts.googleapis.com/css2?family=Exo+2:wght@200;300;400;500&display=swap" rel="stylesheet">
<style>
  :root {
    --stage: #e4e4e4;
    --card-black: #262626;
    --card-grey: #5b5b5e;
    --accent: #d62b2b;
    --ink: #ffffff;
    --back-white: #ffffff;
  }
  * { margin: 0; padding: 0; box-sizing: border-box; }
  html, body { width: 1200px; height: 843px; overflow: hidden; }
  body {
    background: var(--stage);
    font-family: "Exo 2", sans-serif;
    position: relative;
  }
  .card {
    position: absolute;
    top: 72px;
    width: 400px;
    height: 700px;
    overflow: hidden;
    box-shadow: 0 10px 28px rgba(0,0,0,0.18);
  }
  .card--front { left: 230px; background: var(--card-grey); }
  .card--back  { left: 670px; background: var(--back-white); }

  .front-shapes { position: absolute; inset: 0; }

  .brand-name {
    position: absolute;
    top: 42px;
    right: 30px;
    color: var(--ink);
    font-weight: 200;
    font-size: 50px;
    letter-spacing: 0.5px;
  }
  .person {
    position: absolute;
    top: 150px;
    left: 52px;
  }
  .person-name {
    color: var(--accent);
    font-weight: 400;
    font-size: 19px;
    letter-spacing: 1px;
  }
  .person-title {
    color: var(--ink);
    font-weight: 400;
    font-size: 14px;
    letter-spacing: 1px;
    margin-top: 2px;
  }
  .contact-list {
    position: absolute;
    top: 218px;
    left: 30px;
    list-style: none;
  }
  .contact-item {
    display: flex;
    align-items: center;
    gap: 10px;
    color: var(--ink);
    font-size: 13px;
    letter-spacing: 0.6px;
    height: 28px;
  }
  .contact-icon { width: 14px; height: 14px; flex: none; }
  .address {
    position: absolute;
    left: 30px;
    bottom: 74px;
    color: var(--ink);
    font-size: 20px;
    font-weight: 400;
    line-height: 1.45;
    letter-spacing: 0.5px;
  }
</style>
</head>
<body>

<section class="card card--front" aria-label="Card front">
  <svg class="front-shapes" width="400" height="700" viewBox="0 0 400 700">
    <path d="M0 0 H400 V440 C280 520 70 500 0 388 Z" fill="var(--card-black)"/>
    <path d="M0 388 C70 500 280 520 400 440" fill="none" stroke="var(--accent)" stroke-width="6"/>
    <rect x="0" y="664" width="400" height="5" fill="var(--accent)"/>
  </svg>

  <h1 class="brand-name">Velora Salon</h1>

  <div class="person">
    <p class="person-name">JANET REYES</p>
    <p class="person-title">GENERAL MANAGER</p>
  </div>

  <ul class="contact-list">
    <li class="contact-item">
      <svg class="contact-icon" viewBox="0 0 16 16"><path d="M3 1.5 L6 1.5 L7 5 L5.3 6.2 C6.2 8.2 7.8 9.8 9.8 10.7 L11 9 L14.5 10 L14.5 13 C14.5 14 13.5 14.6 12.5 14.4 C7 13.4 2.6 9 1.6 3.5 C1.4 2.5 2 1.5 3 1.5 Z" fill="var(--accent)"/></svg>
      <span>407 531 9264</span>
    </li>
    <li class="contact-item">
      <svg class="contact-icon" viewBox="0 0 16 16"><rect x="4" y="1" width="8" height="14" rx="1.5" fill="var(--accent)"/><rect x="5.5" y="3" width="5" height="8" fill="var(--card-black)"/><circle cx="8" cy="13" r="0.9" fill="var(--card-black)"/></svg>
      <span>407 531 9264</span>
    </li>
    <li class="contact-item">
      <svg class="contact-icon" viewBox="0 0 16 16"><rect x="4" y="1.5" width="8" height="4" fill="var(--accent)"/><rect x="1.5" y="6" width="13" height="6" rx="1" fill="var(--accent)"/><rect x="4" y="10" width="8" height="4.5" fill="var(--accent)" stroke="var(--card-black)" stroke-width="1"/></svg>
      <span>407 531 9264</span>
    </li>
    <li class="contact-item">
      <svg class="contact-icon" viewBox="0 0 16 16"><rect x="1" y="3" width="14" height="10" rx="1" fill="var(--accent)"/><path d="M1.5 3.8 L8 9 L14.5 3.8" fill="none" stroke="var(--card-black)" stroke-width="1.3"/></svg>
      <span>janet@veloraexample.com</span>
    </li>
    <li class="contact-item">
      <svg class="contact-icon" viewBox="0 0 16 16"><circle cx="8" cy="8" r="6.5" fill="none" stroke="var(--accent)" stroke-width="1.5"/><ellipse cx="8" cy="8" rx="2.8" ry="6.5" fill="none" stroke="var(--accent)" stroke-width="1.2"/><line x1="1.5" y1="8" x2="14.5" y2="8" stroke="var(--accent)" stroke-width="1.2"/></svg>
      <span>www.veloraexample.com</span>
    </li>
  </ul>

  <p class="address">214 Linden Ave,<br>2nd floor Suite B.</p>
</section>

<section class="card card--back" aria-label="Card back"></section>

</body>
</html>
```